Architecture firm needing a business card

We need a business card design for a new company based in the US called "Dorrance Architecture". Seeking minimalist designs that have a creativity/design feel but must be clean and professional. Please refer to the logo attached.

Target Market(s)

Real Estate Investors, Home Builders and Construction Firms.

Industry/Entity Type

Architecture

Contact Information for Business Card

Standard US size business cards. Would like to have some sort of graphic on the back side of the card - nothing that is too loud but something that may catch your attention. More or less grayscale colors that are in line with the logo colors (navy and greys essentially). Additional colors maybe accepted if blended properly (earthtones), but might be difficult to accomplish and maintain the clean/minimalist look.

Requirements
Must have
• Clean Lines
Nice to have
• some sort of graphics, would like to have something creative on the back side of the card
Should not have
• nothing too busy, cluttered or overwhelming.

```html
<!DOCTYPE html>
<html lang="en">
<head>
<meta charset="utf-8">
<title>Dorrance Architecture – Business Card</title>
<link rel="stylesheet" href="https://fonts.googleapis.com/css2?family=Open+Sans:wght@400;600&display=swap">
<style>
  :root {
    --page: #e9ebee;
    --navy: #1d4f8c;
    --navy-deep: #153d70;
    --navy-light: #2b70b5;
    --grey: #8c9196;
    --grey-line: #c4c7cb;
    --ink: #4a4d52;
    --paper: #ffffff;
    --blueprint-a: #f4f8fc;
    --blueprint-b: #d6e4f2;
  }
  * { margin: 0; padding: 0; box-sizing: border-box; }
  html, body { width: 1200px; height: 913px; overflow: hidden; }
  body {
    background: var(--page);
    font-family: "Open Sans", sans-serif;
    display: flex;
    flex-direction: column;
    align-items: center;
    justify-content: center;
    gap: 44px;
  }
  .card {
    position: relative;
    width: 680px;
    height: 389px;
    background: var(--paper);
    box-shadow: 0 6px 18px rgba(0,0,0,0.14);
    overflow: hidden;
  }
  .band {
    position: absolute;
    left: 0; right: 0;
    height: 46px;
    background: linear-gradient(90deg, var(--navy-deep), var(--navy), var(--navy-light));
  }
  .band--top { top: 0; border-bottom: 5px solid var(--grey-line); }
  .band--bottom { bottom: 0; border-top: 5px solid var(--grey-line); }

  .blueprint {
    position: absolute;
    left: 0; right: 0; top: 51px; bottom: 51px;
    background: radial-gradient(ellipse at 50% 55%, var(--blueprint-a) 0%, #e9f1f9 45%, var(--blueprint-b) 100%);
  }

  .wordmark {
    position: absolute;
    display: flex;
    align-items: center;
    gap: 14px;
    color: var(--navy);
    font-weight: 400;
  }
  .wordmark__square {
    width: 44px; height: 44px;
    border: 4px solid var(--navy);
  }
  .wordmark__name {
    font-size: 34px;
    line-height: 1.05;
    letter-spacing: 0.04em;
    text-transform: uppercase;
  }
  .wordmark__name span { display: block; font-size: 17px; letter-spacing: 0.38em; }

  .card--front .wordmark { left: 50%; top: 50%; transform: translate(-50%, -50%); }
  .card--back .wordmark { left: 44px; bottom: 84px; }
  .card--back .wordmark__name { font-size: 28px; }
  .card--back .wordmark__name span { font-size: 14px; }
  .card--back .wordmark__square { width: 36px; height: 36px; }

  .contact {
    position: absolute;
    right: 40px;
    top: 74px;
    width: 300px;
    color: var(--ink);
  }
  .contact__name {
    font-size: 21px;
    letter-spacing: 0.02em;
    text-transform: uppercase;
    color: var(--ink);
  }
  .contact__name b { font-weight: 600; }
  .contact__role {
    font-size: 11px;
    letter-spacing: 0.08em;
    text-transform: uppercase;
    color: var(--grey);
    padding-bottom: 8px;
    border-bottom: 1.5px solid var(--navy);
  }
  .contact__list { list-style: none; margin-top: 16px; }
  .contact__item {
    display: flex;
    align-items: center;
    gap: 12px;
    margin-bottom: 12px;
    font-size: 13px;
    line-height: 1.35;
  }
  .contact__icon {
    flex: none;
    width: 28px; height: 28px;
    border-radius: 5px;
    background: var(--navy);
    display: flex; align-items: center; justify-content: center;
  }
</style>
</head>
<body>

<section class="card card--front" aria-label="Card front">
  <div class="band band--top"></div>
  <div class="blueprint" role="img" aria-label="Faint blue architectural floor plan drawing"></div>
  <div class="wordmark">
    <div class="wordmark__square"></div>
    <div class="wordmark__name">Dorrance<span>Architecture</span></div>
  </div>
  <div class="band band--bottom"></div>
</section>

<section class="card card--back" aria-label="Card back">
  <div class="band band--top"></div>

  <div class="contact">
    <p class="contact__name"><b>Miles</b> Harlan</p>
    <p class="contact__role">Creative Director</p>
    <ul class="contact__list">
      <li class="contact__item">
        <span class="contact__icon">
          <svg width="16" height="16" viewBox="0 0 24 24" fill="#fff"><path d="M6.6 10.8a15.1 15.1 0 0 0 6.6 6.6l2.2-2.2a1 1 0 0 1 1-.25 11.4 11.4 0 0 0 3.6.57 1 1 0 0 1 1 1V20a1 1 0 0 1-1 1A17 17 0 0 1 3 4a1 1 0 0 1 1-1h3.5a1 1 0 0 1 1 1c0 1.25.2 2.45.57 3.57a1 1 0 0 1-.25 1z"/></svg>
        </span>
        <span>555 . 0142 . 7780<br>555 . 0142 . 7781</span>
      </li>
      <li class="contact__item">
        <span class="contact__icon">
          <svg width="16" height="16" viewBox="0 0 24 24" fill="none" stroke="#fff" stroke-width="2"><circle cx="12" cy="12" r="9"/><path d="M3 12h18M12 3c3 3.5 3 14.5 0 18M12 3c-3 3.5-3 14.5 0 18"/></svg>
        </span>
        <span>studio@dorrancearch.com<br>www.dorrancearch.com</span>
      </li>
      <li class="contact__item">
        <span class="contact__icon">
          <svg width="16" height="16" viewBox="0 0 24 24" fill="#fff"><path d="M12 2a7 7 0 0 0-7 7c0 5.2 7 13 7 13s7-7.8 7-13a7 7 0 0 0-7-7zm0 9.5A2.5 2.5 0 1 1 12 6.5a2.5 2.5 0 0 1 0 5z"/></svg>
        </span>
        <span>17 Alder Lane<br>Tampa FL 33601</span>
      </li>
    </ul>
  </div>

  <div class="wordmark">
    <div class="wordmark__square"></div>
    <div class="wordmark__name">Dorrance<span>Architecture</span></div>
  </div>

  <div class="band band--bottom"></div>
</section>

</body>
</html>
```